Postcard Design

KVO Ltd are a screen and large format digital company that specialise is direct to substrate marketing. I would like a postcard design to send to clients with every job we send out, informing them of other items we can do.
From conventional screen printing to digital printing from vehicle graphics to glass printing, from exhibition panels to window graphics, banners etc.
You can read more on our web site www.kvo-ltd.com
Emphasis on dealing directly with the printers instead of using a middle marketing company
we like the back to be a reply card , with the logo but like the idea or the paper looking scrunched up as in the brisk lantern advert.
hi re logo to be used as supplied

Target Market(s)

Other printers who we trade print for and Marketing agencies

Industry/Entity Type

Screen Printing

Requirements
Must have
• Company logo
Nice to have
• Something different.......BE BOLD, almost quirky
Should not have
• the usual Printers CMYK cack

```html
<!DOCTYPE html>
<html lang="en">
<head>
<meta charset="utf-8">
<title>KVO Ltd Reply Postcard</title>
<link rel="stylesheet" href="https://fonts.googleapis.com/css2?family=Neucha&family=Special+Elite&display=swap">
<style>
  :root {
    --page-bg: #ffffff;
    --card-bg: #000000;
    --headline: #fdf7c8;
    --ink-light: #ffffff;
    --rule: #9a9a9a;
    --stamp-line: #b5b5b5;
    --note: #d6d6d6;
    --badge: #fbf3c4;
  }
  html, body {
    margin: 0;
    padding: 0;
    width: 1200px;
    height: 961px;
    overflow: hidden;
    background: var(--page-bg);
  }
  .postcard {
    position: absolute;
    left: 101px;
    top: 184px;
    width: 980px;
    height: 652px;
    background: var(--card-bg);
    overflow: hidden;
    font-family: "Neucha", cursive;
  }
  .stamp-box {
    position: absolute;
    left: 869px;
    top: 14px;
    width: 92px;
    height: 92px;
    border: 1px solid var(--stamp-line);
    box-sizing: border-box;
  }
  .brand {
    position: absolute;
    left: 0;
    right: 0;
    top: 36px;
    display: flex;
    justify-content: center;
    align-items: center;
    gap: 18px;
  }
  .brand-dot {
    width: 100px;
    height: 100px;
    border-radius: 50%;
    background: var(--badge);
  }
  .brand-name {
    font-family: "Neucha", cursive;
    font-size: 54px;
    color: var(--badge);
    line-height: 1;
  }
  .headline {
    position: absolute;
    left: 0;
    right: 0;
    top: 194px;
    margin: 0;
    text-align: center;
    white-space: nowrap;
    font-family: "Neucha", cursive;
    font-weight: 400;
    font-size: 66px;
    line-height: 66px;
    color: var(--headline);
    z-index: 1;
  }
  .divider {
    position: absolute;
    left: 0;
    top: 246px;
    width: 100%;
    height: 1px;
    background: var(--rule);
  }
  .contact {
    position: absolute;
    left: 52px;
    top: 376px;
    margin: 0;
    font-style: normal;
    font-size: 29px;
    line-height: 38px;
    color: var(--ink-light);
  }
  .reply-lines {
    position: absolute;
    left: 562px;
    top: 0;
    width: 400px;
    height: 100%;
  }
  .reply-line {
    position: absolute;
    left: 0;
    width: 100%;
    height: 1px;
    background: var(--rule);
  }
  .reply-line.l1 { top: 388px; }
  .reply-line.l2 { top: 440px; }
  .reply-line.l3 { top: 492px; }
  .reply-line.l4 { top: 536px; }
  .quote-note {
    position: absolute;
    left: 753px;
    top: 453px;
    margin: 0;
    transform: translate(-50%, -50%) rotate(-30deg);
    white-space: nowrap;
    font-family: "Special Elite", monospace;
    font-size: 18px;
    letter-spacing: 0.5px;
    color: var(--note);
  }
  .website {
    position: absolute;
    left: 0;
    width: 980px;
    top: 594px;
    text-align: center;
    font-size: 31px;
    line-height: 38px;
    color: var(--ink-light);
  }
</style>
</head>
<body>
  <main class="postcard">
    <div class="stamp-box"></div>

    <div class="brand">
      <div class="brand-dot"></div>
      <div class="brand-name">KVO Ltd</div>
    </div>

    <h1 class="headline">The Latest In Digital Print Technology</h1>
    <div class="divider"></div>

    <address class="contact">
      18 Harlow Row, Brentfield,<br>
      Surrey, BF2 7QL<br>
      Tel: 020 7946 0321<br>
      E-mail: info@kvo-ltd.com
    </address>

    <div class="reply-lines">
      <div class="reply-line l1"></div>
      <div class="reply-line l2"></div>
      <div class="reply-line l3"></div>
      <div class="reply-line l4"></div>
    </div>

    <p class="quote-note">Please call or email for quotations</p>

    <div class="website">www.kvo-ltd.com</div>
  </main>
</body>
</html>
```